University of Marrowvale Club Rowing Team - Fundraising Poster

GREAT OPPORTUNITY FOR SPORTS DESIGNERS

The University of Marrowvale club rowing team is holding a fundraising event – The Grand Distance

Push. As a team we will collectively row one million meters on indoor rowing machines.

We are looking for an eye catching poster that incorporates the following aspects in a creative way:

>> Designs MAY NOT include any University of Marrowvale logos or fonts. The club rowing team is not affiliated with the athletic department.

>> Suggested fonts are Microgramma and AkzidenzGroteskBE-Bold.

>> The event will take place on Pelling Basketball Court on February 15th

>> Features of the event include a “Beat the Crew” competition, a pasta meal, and a raffle and silent auction with prizes from local businesses.

>> UM school colors are lightning yellow (# fce122) and thunder green (# 18453b), although eye-catching designs with different color schemes are welcome.

>> The event is titled “The Grand Distance Push”, it also may be referred to as an Erg-a-thon, or Grand Distance Push. Experiment with it.

>> Successful designs will include elements related to the sport of rowing (mainly) rowing machines, but also oars, boats, etc.

>>This event is funded by the Heron Activities Fund, and the attached logo must be incorporated into the design in some way (the bottom corner is fine). Consider leaving space at the bottom footer for additional sponsor logos.

Design ideas we’re interested in:

1.) An 8 x 10 poster, a traditional erg-a-thon poster that includes people on a rowing machine and heavily utilizes the school colors listed above. See seconddesign images for inspiration.

2.) An 8 x 10 poster with minimalist design that features a hardwood basketball court with a single rowing machine spotlighted in the center with text above reading “University of Marrowvale Club Rowing Presents:” and below reading “One Grand Distance Push, find out more at Pelling Court February 15th”. Looking for something similar to hard court spotlight ads attached.

3.) An 8x10 unique rowing poster which stands out as something eye catching and creative. Examples posted as example3.1/3.2 for inspiration.

Also Images of Vantor 5 Rowing Machines Attached

Target Market(s)

College Students, Program Alumni, Local Community

Industry/Entity Type

School

Requirements
Must have
• University of Marrowvale Club Rowing, Heron Activity's Fund Logo, Ergathon or Grand Distance Push, Winning Design will almost certainly feature a vantor 5 rowing machine
Should not have
• University of Marrowvale Logo, School or Athletic Department Fonts

```html
<!DOCTYPE html>
<html lang="en">
<head>
<meta charset="utf-8">
<title>The Grand Distance Push – Poster</title>
<link rel="stylesheet" href="https://fonts.googleapis.com/css2?family=Orbitron:wght@500;600;700;900&display=swap">
<style>
  :root {
    --backdrop: #262626;
    --ink-black: #050505;
    --lightning-yellow: #fce122;
    --paper-white: #ffffff;
    --soft-grey: #cfcfcf;
    --tan-copy: #b9a190;
    --wood-dark: #3a2012;
    --wood-mid: #7a4a2a;
    --machine-dark: #2a2a2a;
    --machine-mid: #4a4a4a;
    --court-line: rgba(70,70,70,.55);
    --fund-green: #5cc49a;
  }
  * { margin: 0; padding: 0; box-sizing: border-box; }
  html, body {
    width: 1200px; height: 1000px; overflow: hidden;
    background: var(--backdrop);
  }
  .poster {
    position: absolute; left: 259px; top: 72px;
    width: 691px; height: 864px;
    background: var(--ink-black);
    overflow: hidden;
    box-shadow: 0 4px 14px rgba(0,0,0,.5);
  }
  .court-scene {
    position: absolute; inset: 0;
    background: linear-gradient(to bottom,
      #030303 0%, #0a0a0a 44%, #7d7d7d 48%, #eeeeee 53%, #f2f2f2 60%,
      #b5b5b5 66%, #2a211b 72%, var(--wood-dark) 76%, var(--wood-mid) 84%,
      #9a6c50 90%, #f4f0ec 96%, #ffffff 100%);
  }
  .court-circle {
    position: absolute; left: 0; top: 0; width: 691px; height: 864px;
  }
  .machine-placeholder {
    position: absolute; left: 156px; top: 433px;
    width: 372px; height: 165px;
    border-radius: 40px;
    background: radial-gradient(ellipse at 55% 60%, var(--machine-mid) 0%, var(--machine-dark) 55%, rgba(42,42,42,.0) 100%);
  }
  .presenter {
    position: absolute; left: 141px; top: 106px;
    font-family: "Orbitron", sans-serif; font-weight: 600;
    font-size: 11.5px; color: var(--soft-grey);
  }
  .title {
    position: absolute; left: 145px; top: 152px;
    font-family: "Orbitron", sans-serif; font-weight: 900;
    text-transform: uppercase; line-height: 1;
  }
  .title span { display: block; }
  .title .accent { color: var(--lightning-yellow); font-size: 42px; height: 56px; }
  .title .main { color: var(--paper-white); font-size: 60px; height: 66px; }
  .title .main.long { font-size: 54px; }
  .event-info {
    position: absolute; left: 147px; top: 645px;
    font-family: "Orbitron", sans-serif;
  }
  .venue { font-size: 15px; font-weight: 700; color: var(--paper-white); }
  .venue .date { color: var(--lightning-yellow); }
  .features {
    margin-top: 7px; font-size: 11px; font-weight: 600;
    line-height: 17px; color: var(--tan-copy);
  }
  .fund-mark {
    position: absolute; left: 62px; top: 795px; width: 58px;
    display: flex; flex-direction: column; align-items: center; gap: 3px;
  }
  .fund-mark .square { width: 58px; height: 25px; background: var(--fund-green); }
  .fund-mark .name {
    font-family: "Orbitron", sans-serif; font-weight: 700; font-size: 4px;
    color: var(--fund-green); white-space: nowrap;
  }
</style>
</head>
<body>
  <main class="poster">
    <div class="court-scene" role="img" aria-label="Hardwood basketball court in darkness under a single spotlight"></div>

    <svg class="court-circle" viewBox="0 0 691 864" aria-hidden="true">
      <ellipse cx="341" cy="583" rx="248" ry="32" fill="none" stroke="var(--court-line)" stroke-width="3"/>
    </svg>

    <div class="machine-placeholder" role="img" aria-label="Vantor 5 indoor rowing machine standing in the spotlight at centre court"></div>

    <p class="presenter">University of Marrowvale Club Rowing presents</p>

    <h1 class="title">
      <span class="accent">The</span>
      <span class="main">Grand</span>
      <span class="main long">Distance</span>
      <span class="accent">Push</span>
    </h1>

    <section class="event-info">
      <p class="venue">Pelling Basketball Court <span class="date">February 15</span></p>
      <p class="features">Beat the Crew competition, a pasta meal, and a raffle<br>and a silent auction with prizes from local businesses</p>
    </section>

    <div class="fund-mark">
      <span class="square"></span>
      <span class="name">HERON ACTIVITIES FUND</span>
    </div>
  </main>
</body>
</html>
```